Creative Stationary for Solo Law Firm

I am looking for stationary designs for my solo law firm called TM Halvorsen Law PLLC. My logo is attached. I'd like the logo incorporated into the design.

I'm looking for a stationary design that is a bit outside of the box and not too standard or boring. The final design should communicate professionalism.

Target Market(s)

United States Clients, Opposing Counsel

Industry/Entity Type

Legal

Font styles to use
Sans Serif

Requirements
Must have
• The stationary design must incorporate my logo design attached. The design itself must be creative. The envelope design must follow standard United States designs with room for the postage stamp at the top right corner and space for the recipient's address in the middle.

```html
<!DOCTYPE html>
<html lang="en">
<head>
<meta charset="utf-8">
<title>TM Halvorsen Law – Business Card</title>
<link href="https://fonts.googleapis.com/css2?family=Arimo:wght@400;700&display=swap" rel="stylesheet">
<style>
  :root {
    --navy: #1b2766;
    --grey-text: #8a8d93;
    --card: #fbfbfb;
    --backdrop: #e4e5e8;
    --shadow: rgba(30, 35, 50, 0.14);
  }
  * { margin: 0; padding: 0; box-sizing: border-box; }
  html, body {
    width: 1200px; height: 900px; overflow: hidden;
    background: var(--backdrop);
    font-family: "Arimo", Arial, sans-serif;
  }
  .sheet {
    position: relative; width: 1200px; height: 900px;
    display: flex; align-items: center; justify-content: center; gap: 40px;
  }
  .card {
    position: relative; width: 540px; height: 309px;
    background: var(--card);
    box-shadow: 0 10px 28px var(--shadow), 0 1px 3px var(--shadow);
  }
  .wordmark {
    position: absolute;
    color: var(--navy);
    font-weight: 400;
    font-size: 25px;
    line-height: 1;
    letter-spacing: 0.04em;
    text-transform: uppercase;
    white-space: nowrap;
  }
  .accent-bar {
    position: absolute; width: 4px; height: 30px; background: var(--navy);
  }
  .website {
    position: absolute; font-size: 13px; line-height: 1; letter-spacing: 0.08em;
    color: var(--grey-text); white-space: nowrap;
  }
  .website strong { color: var(--navy); font-weight: 700; }

  /* back */
  .card--back .website { right: 80px; top: 124px; }
  .card--back .accent-bar { right: 56px; top: 116px; }
  .card--back .wordmark { left: 130px; top: 200px; }

  /* front */
  .card--front .wordmark { left: 44px; top: 72px; }
  .holder { position: absolute; left: 66px; top: 152px; }
  .holder__name { color: var(--navy); font-size: 14px; letter-spacing: 0.02em; text-transform: uppercase; }
  .holder__title { color: var(--grey-text); font-size: 12px; letter-spacing: 0.04em; text-transform: uppercase; margin-top: 3px; }
  .address { position: absolute; left: 66px; top: 214px; color: var(--grey-text); font-size: 13px; line-height: 1.4; }
  .card--front .accent-bar { left: 44px; top: 218px; }
  .contact { position: absolute; left: 340px; top: 134px; color: var(--grey-text); font-size: 13px; line-height: 1.5; }
  .contact__row { display: flex; align-items: center; gap: 8px; white-space: nowrap; }
  .contact__row svg { width: 11px; height: 11px; fill: var(--navy); flex: none; }
</style>
</head>
<body>
<main class="sheet">
  <section class="card card--back" aria-label="Card back">
    <div class="website">www.<strong>tm-halvorsen</strong>.com</div>
    <div class="accent-bar"></div>
    <div class="wordmark">TM Halvorsen Law</div>
  </section>

  <section class="card card--front" aria-label="Card front">
    <div class="wordmark">TM Halvorsen Law</div>
    <div class="holder">
      <div class="holder__name">Martin Halvorsen</div>
      <div class="holder__title">President</div>
    </div>
    <div class="address">2210 Birchwood Avenue<br>Suite 200, Larchmont, NY 10538</div>
    <div class="accent-bar"></div>
    <div class="contact">
      <div class="contact__row">
        <svg viewBox="0 0 24 24" aria-hidden="true"><path d="M6.6 10.8a15.1 15.1 0 0 0 6.6 6.6l2.2-2.2a1 1 0 0 1 1-.25 11.4 11.4 0 0 0 3.6.57 1 1 0 0 1 1 1V20a1 1 0 0 1-1 1A17 17 0 0 1 3 4a1 1 0 0 1 1-1h3.5a1 1 0 0 1 1 1c0 1.250.2 2.450.57 3.57a1 1 0 0 1-.25 1z"/></svg>
        <span>914-555-0148</span>
      </div>
      <div class="contact__row">
        <svg viewBox="0 0 24 24" aria-hidden="true"><path d="M2 5h20v14H2zm2 2v.5l8 5 8-5V7l-8 5z"/></svg>
        <span>martin@tm-halvorsen.com</span>
      </div>
    </div>
  </section>
</main>
</body>
</html>
```